qvbn website

revamp of existing website...design only
quobrin.com.au
existing site a bit óld fashioned'...needs to be modernised and bright and cheery.
need: home page, second and third level pages.

Target Market(s)

end user/retail information website
this site does NOT need a shopping card as we do not sell direct to the public

Requirements
Must have
• 3 levels
• home
• second level
• third level

```html
<!DOCTYPE html>
<html lang="en">
<head>
<meta charset="utf-8">
<title>Quobrin – Metal Storage Cabinets</title>
<link rel="stylesheet" href="https://fonts.googleapis.com/css2?family=PT+Sans:wght@400;700&family=PT+Sans+Narrow:wght@400;700&display=swap">
<style>
:root{
  --red:#e8202c;
  --red-light:#f43a44;
  --red-dark:#a90c12;
  --ink:#111;
  --grey:#666;
  --grey-mid:#888;
  --line:#e2e2e2;
  --panel:#f4f4f4;
  --nav:#2a2a2a;
  --yellow:#ffd21f;
  --white:#fff;
}
*{box-sizing:border-box;margin:0;padding:0}
html,body{width:1147px;height:1200px;overflow:hidden}
body{position:relative;background:var(--white);font-family:"PT Sans",sans-serif;color:var(--grey)}
a{color:inherit;text-decoration:none}
.header-band{position:absolute;left:0;top:0;width:1147px;height:278px;background:linear-gradient(#f4424b,var(--red) 60%,#e2141f)}
.utility{position:absolute;right:111px;top:14px;font-size:12.5px;color:var(--white)}
.utility span{margin:0 5px}
.brand{position:absolute;left:100px;top:32px}
.brand-name{font-family:"PT Sans Narrow",sans-serif;font-weight:700;font-size:66px;line-height:1;color:var(--white);letter-spacing:4px;text-transform:uppercase}
.brand-tag{position:absolute;left:155px;top:66px;white-space:nowrap;font-family:"PT Sans Narrow",sans-serif;font-weight:700;font-size:21px;color:var(--yellow)}
.call{position:absolute;right:111px;top:70px;text-align:right;color:var(--white);font-family:"PT Sans Narrow",sans-serif}
.call-label{font-size:18px;line-height:1}
.call-number{font-size:30px;font-weight:700;line-height:1.1}
.main-nav{position:absolute;left:100px;top:132px;width:944px;height:47px;background:linear-gradient(#3a3a3a,#1b1b1b);border-radius:4px 4px 0 0;display:flex}
.main-nav a{font-family:"PT Sans Narrow",sans-serif;font-size:16.5px;color:var(--white);line-height:47px;padding:0 11px;border-right:1px solid #555;text-transform:uppercase;white-space:nowrap}
.main-nav a:first-child{padding-left:29px}
.main-nav a:last-child{border-right:0}
.page{position:absolute;left:100px;top:179px;width:944px;height:901px;background:var(--white);box-shadow:0 0 6px rgba(0,0,0,.08)}
.hero{position:absolute;left:0;top:0;width:944px;height:351px;background:linear-gradient(#fff 60%,#ececec);border-bottom:1px solid #ddd}
.hero-text{position:absolute;left:64px;top:99px;font-family:"PT Sans Narrow",sans-serif;font-weight:700;line-height:1}
.hero-kicker{font-size:29px;color:var(--grey-mid)}
.hero-title{font-size:45px;color:#d0141d;margin-top:2px}
.hero-sub{font-size:29px;color:#d0141d;margin-top:4px}
.hero-image{position:absolute;left:566px;top:36px;width:320px;height:280px;border-radius:3px;background:linear-gradient(135deg,#f0f0f0,#cfd1d3)}
.dots{position:absolute;left:436px;top:322px;display:flex;gap:2px}
.dots span{width:13px;height:13px;border-radius:50%;background:#9a9a9a}
.welcome{position:absolute;left:28px;top:386px;width:610px}
.welcome h1{font-family:"PT Sans Narrow",sans-serif;font-weight:700;font-size:29px;color:var(--ink);text-transform:uppercase;line-height:1;margin-bottom:8px}
.welcome p{font-size:13px;line-height:21.3px;margin-bottom:8px}
.card{position:absolute;background:linear-gradient(#fff,var(--panel));border:1px solid var(--line);border-radius:4px}
.card h2{font-weight:400;font-size:23px;color:#d0141d;font-family:"PT Sans Narrow",sans-serif}
.brochure{left:656px;top:380px;width:271px;height:176px;padding:18px 22px}
.brochure h2{font-weight:700;margin-bottom:4px}
.brochure p{font-size:13px;line-height:21.3px}
.btn{display:inline-block;margin-top:8px;background:linear-gradient(#e6242d,#c10c14);color:var(--white);font-weight:700;font-size:13.5px;padding:9px 16px;border-radius:3px;text-transform:uppercase}
.products{left:27px;top:573px;width:612px;height:289px;padding:18px 26px}
.product-row{display:flex;margin-top:12px;border:1px solid var(--line);width:560px;background:var(--white)}
.product{width:140px;border-right:1px solid var(--line)}
.product:last-child{border-right:0}
.product-image{height:129px;border-bottom:1px solid var(--line);display:flex;align-items:center;justify-content:center}
.product-image div{width:70px;height:110px;background:linear-gradient(135deg,#eee,#bfc1c3);border-radius:2px}
.product h3{font-family:"PT Sans Narrow",sans-serif;font-weight:400;font-size:16.5px;color:#d0141d;padding:10px 15px 2px}
.product p{font-size:11px;line-height:16px;color:var(--grey-mid);padding:0 15px 16px}
.lockable{left:656px;top:573px;width:271px;height:289px;padding:18px 22px}
.lockable ul{list-style:none;margin-top:6px}
.lockable li{font-size:13px;color:#333;line-height:24px;border-bottom:1px solid #e6e6e6;padding-left:13px;position:relative;width:224px}
.lockable li:last-child{border-bottom:0}
.lockable li::before{content:"";position:absolute;left:0;top:8px;border-left:5px solid #999;border-top:4px solid transparent;border-bottom:4px solid transparent}
.footer{position:absolute;left:0;top:1080px;width:1147px;height:120px;background:linear-gradient(#c8141c,var(--red-dark));border-top:4px solid #ddd}
.footer-nav{position:absolute;left:126px;top:33px;font-family:"PT Sans Narrow",sans-serif;font-size:14px;color:var(--white);text-transform:uppercase;white-space:nowrap}
.footer-nav span{margin:0 4px}
.copyright{position:absolute;left:126px;top:64px;font-size:10.5px;color:var(--white)}
.social{position:absolute;left:916px;top:29px;display:flex;gap:3px}
.social span{width:26px;height:26px;border-radius:50%;background:var(--white)}
</style>
</head>
<body>
<header>
  <div class="header-band"></div>
  <div class="utility"><a href="#">Email Us</a><span>|</span><a href="#">Shopping Cart</a></div>
  <div class="brand">
    <div class="brand-name">Quobrin</div>
    <div class="brand-tag">METAL STORAGE CABINETS</div>
  </div>
  <div class="call">
    <div class="call-label">CALL US NOW</div>
    <div class="call-number">1300.482.615</div>
  </div>
  <nav class="main-nav">
    <a href="#">Home</a><a href="#">Style 1</a><a href="#">Style 2</a><a href="#">Style 3</a><a href="#">Counter Height</a><a href="#">Half Width</a><a href="#">Style 5K</a><a href="#">Style 6K</a><a href="#">Where to Buy</a><a href="#">Who Are We</a>
  </nav>
</header>

<main class="page">
  <section class="hero">
    <div class="hero-text">
      <div class="hero-kicker">METAL STORAGE CABINETS</div>
      <div class="hero-title">NARROW SPACE?</div>
      <div class="hero-sub">HALF WIDTH UNITS FIT THE SPACE !</div>
    </div>
    <div class="hero-image" role="img" aria-label="Photo of white metal storage cabinets, open and closed, with files on shelves"></div>
    <div class="dots"><span></span><span></span><span></span><span></span><span></span></div>
  </section>

  <section class="welcome">
    <h1>Welcome to Quobrin Mainpage..</h1>
    <p>Duis tincidunt lectus quis dui viverra vestibulum. Suspendisse vulputate aliquam dui. Nulla elementum dui ut augue. Aliquam vehicula mi at mauris. Maecenas placerat, nisl at consequat rhoncus, sem nunc gravida justo, quis eleifend arcu velit quis lacus. Morbi magna magna, tincidunt a, mattis non, imperdiet vitae, tellus. Sed odio est, auctor ac, sollicitudin in, consequat vitae, orci. Fusce id felis. Vivamus sollicitudin metus eget eros</p>
    <p>Etiam eu urna. Sed porta. Suspendisse quam leo, molestie sed, luctus quis, feugiat in, pede.</p>
  </section>

  <aside class="card brochure">
    <h2>Dowload Brochure</h2>
    <p>Fusce tellus Sed metus augue convallis et vehicula ut pulvinar eu ante Integer orci tellus tristique.</p>
    <a class="btn" href="#">Download Now</a>
  </aside>

  <section class="card products">
    <h2>Latest Products</h2>
    <div class="product-row">
      <div class="product"><div class="product-image"><div role="img" aria-label="Tall open metal cabinet with shelves"></div></div><h3>Product Name</h3><p>Fusce tellus Sed metus augue convallis</p></div>
      <div class="product"><div class="product-image"><div role="img" aria-label="Cream counter height metal cabinet" style="width:80px;height:90px"></div></div><h3>Product Name</h3><p>Fusce tellus Sed metus augue convallis</p></div>
      <div class="product"><div class="product-image"><div role="img" aria-label="Tall grey metal cabinet with open doors"></div></div><h3>Product Name</h3><p>Fusce tellus Sed metus augue convallis</p></div>
      <div class="product"><div class="product-image"><div role="img" aria-label="Wide steel cabinet with open doors" style="width:110px;height:95px"></div></div><h3>Product Name</h3><p>Fusce tellus Sed metus augue convallis</p></div>
    </div>
  </section>

  <aside class="card lockable">
    <h2>Lockable Storage For</h2>
    <ul>
      <li>Power Tools</li><li>Spare Parts</li><li>Workshop Grease &amp; Oil</li><li>Sports Equipment</li><li>Office Stationery</li><li>Picnic and BBQ tools</li><li>Swimming Pool Salt</li><li>Business Records</li><li>Filing</li>
    </ul>
  </aside>
</main>

<footer class="footer">
  <div class="footer-nav">Home<span>|</span>Style 1<span>|</span>Style 2<span>|</span>Style 3<span>|</span>Counter Height<span>|</span>Half Width<span>|</span>Style 5K<span>|</span>Style 6K<span>|</span>Where to Buy<span>|</span>Who Are We</div>
  <div class="copyright">© 2012 Company Name.&nbsp; All right reserved.&nbsp; Term of Use</div>
  <div class="social"><span></span><span></span><span></span><span></span></div>
</footer>
</body>
</html>
```